DRUM needs a contemporary simple brochure

We help companies understand their customers, and we would like to send a minimalistic card/brochure to potential clients to introduce our company. The card will be A6 in size (ie A5 folded once) and so will have a front, an inside front, and inside back, and a back page. It can either be portrait or landscape.
It should convey contemporary/modern, bold, fun, uncomplicated/simplicity, be clean/uncluttered, and use friendly and easy to read fonts.
Attached is the information the brochure/card should contain, together with colour palatte and another document which shows our logo, existing stationary etc to give you a feel of the brand. The background of the card could be black, yellow or white (or a combination). thanks, mark
Updates
Hi everyone. Just to let you know that the card will be A6 size, will have a matt laminate finish and can include spot uv. thanks, mark
Reason: Hi, I am looking for some better quality designs so i have extended the deadline and significantly increased the budget. thanks, mark
Target Market(s)
Marketing professionals in large corporates
Industry/Entity Type
It Company
Requirements
Must have
- use our company colours (attached)

```html
<!DOCTYPE html>
<html lang="en">
<head>
<meta charset="utf-8">
<title>DRUM – Customer &amp; Shopper Market Research brochure</title>
<link rel="stylesheet" href="https://fonts.googleapis.com/css2?family=Archivo+Black&family=Arimo:wght@400;700&display=swap">
<style>
  :root{
    --yellow:#f7c600;
    --yellow-light:#ffd928;
    --yellow-deep:#e0a800;
    --black:#0d0d0d;
    --charcoal:#2a2a2a;
    --grey:#6f6f6f;
    --stage:#8a8a8a;
    --white:#ffffff;
  }
  *{margin:0;padding:0;box-sizing:border-box}
  html,body{width:1200px;height:844px;overflow:hidden}
  body{
    background:radial-gradient(ellipse at 50% 45%, #9a9a9a 0%, var(--stage) 55%, #5e5e5e 100%);
    font-family:"Arimo", Arial, sans-serif;
  }
  .spread{
    position:absolute;left:180px;top:125px;width:840px;height:594px;
    display:flex;box-shadow:0 18px 40px rgba(0,0,0,.35);
  }
  .panel{position:relative;width:420px;height:594px;overflow:hidden}
  .panel > svg.bg{position:absolute;inset:0}
  .fold{position:absolute;left:418px;top:0;width:4px;height:594px;
    background:linear-gradient(90deg,rgba(0,0,0,0),rgba(0,0,0,.18),rgba(0,0,0,0));z-index:5}

  /* company name */
  .brand-name{position:absolute;font-family:"Archivo Black", Arial, sans-serif;line-height:1;letter-spacing:1px;text-transform:uppercase}
  .tagline{position:absolute;font-size:14px;letter-spacing:.3px}

  /* front */
  .front .brand-name{left:62px;top:58px;font-size:60px;color:var(--yellow)}
  .front .tagline{left:66px;top:126px;color:var(--yellow)}
  .headline{
    position:absolute;left:40px;right:28px;top:300px;text-align:right;
    font-family:"Archivo Black", Arial, sans-serif;color:var(--black);line-height:1
  }
  .headline .small{display:block;font-size:28px;margin-bottom:4px;padding-right:30px}
  .headline .big{display:block;font-size:52px;letter-spacing:-.5px}
  .web{position:absolute;color:var(--white);font-size:13px;font-weight:700;letter-spacing:4px}
  .front .web{left:150px;top:549px}

  /* back */
  .tile{position:absolute;border-radius:14px;border:3px solid var(--white);box-shadow:0 3px 8px rgba(0,0,0,.3)}
  .tile-family{left:40px;top:100px;width:105px;height:100px;background:linear-gradient(135deg,#c9735a,#e6a67a 50%,#7a5a8a)}
  .tile-office{left:125px;top:32px;width:95px;height:88px;background:linear-gradient(160deg,#d9dde3,#4a5566)}
  .tile-dining{left:158px;top:132px;width:90px;height:100px;background:linear-gradient(150deg,#e9e3d6,#6b3b22)}
  .tile-words{left:75px;top:210px;width:100px;height:100px;background:linear-gradient(135deg,#f3f3f3,#bdbdbd)}
  .back .brand-name{left:120px;top:326px;font-size:50px;color:var(--white)}
  .back .tagline{left:124px;top:384px;color:var(--white);font-size:12px}
  .divider{position:absolute;left:100px;top:405px;width:210px;height:1px;background:rgba(255,255,255,.6)}
  .contact{position:absolute;left:120px;top:420px;color:var(--white);list-style:none}
  .contact li{display:flex;align-items:flex-start;gap:8px;margin-bottom:10px;font-size:12px;line-height:1.3}
  .contact li.phone{font-size:19px;font-weight:700;align-items:center}
  .contact svg{flex:none;margin-top:1px}
  .back .web{left:120px;top:549px}
</style>
</head>
<body>
<main class="spread">

  <section class="panel back" aria-label="Back cover">
    <svg class="bg" width="420" height="594" viewBox="0 0 420 594">
      <defs>
        <radialGradient id="backYellow" cx="45%" cy="35%" r="75%">
          <stop offset="0" stop-color="#ffd928"/>
          <stop offset="1" stop-color="#e0a800"/>
        </radialGradient>
      </defs>
      <rect width="420" height="594" fill="url(#backYellow)"/>
      <path d="M40 540 L420 528 L420 572 L70 584 Z" fill="#0d0d0d"/>
    </svg>

    <div class="tile tile-family" role="img" aria-label="Photo of a family reading together"></div>
    <div class="tile tile-office" role="img" aria-label="Photo of a business team around a laptop"></div>
    <div class="tile tile-dining" role="img" aria-label="Photo of a plated meal and a glass of wine"></div>
    <div class="tile tile-words" role="img" aria-label="Word cloud of online marketing terms"></div>

    <p class="brand-name">Drum</p>
    <p class="tagline">customer insight</p>
    <div class="divider"></div>

    <ul class="contact">
      <li>
        <svg width="14" height="13" viewBox="0 0 14 13"><path d="M7 0 L14 6 H12 V13 H8.5 V9 H5.5 V13 H2 V6 H0 Z" fill="#fff"/></svg>
        <span>Level 4, 27 Harbour Lane,<br>Rivergate, NSW, 2099</span>
      </li>
      <li class="phone">
        <svg width="14" height="16" viewBox="0 0 14 16"><path d="M3 0 L6 4 L4.5 6 C5.5 8.5 7 10 9 11 L11 9.5 L14 12.5 L12 15.5 C6 15 1 9 0.5 3 Z" fill="#fff"/></svg>
        <span>02 9555 0147</span>
      </li>
      <li>
        <svg width="15" height="11" viewBox="0 0 15 11"><rect x=".75" y=".75" width="13.5" height="9.5" fill="none" stroke="#fff" stroke-width="1.5"/><path d="M1 1 L7.5 6.5 L14 1" fill="none" stroke="#fff" stroke-width="1.5"/></svg>
        <span>info@drummr.com.au</span>
      </li>
    </ul>

    <p class="web">www.drummr.com.au</p>
  </section>

  <div class="fold"></div>

  <section class="panel front" aria-label="Front cover">
    <svg class="bg" width="420" height="594" viewBox="0 0 420 594">
      <defs>
        <radialGradient id="frontYellow" cx="45%" cy="60%" r="70%">
          <stop offset="0" stop-color="#ffd928"/>
          <stop offset="1" stop-color="#e0a800"/>
        </radialGradient>
        <linearGradient id="blackTop" x1="0" y1="0" x2="0" y2="1">
          <stop offset="0" stop-color="#1e1e1e"/>
          <stop offset="1" stop-color="#0d0d0d"/>
        </linearGradient>
      </defs>
      <rect width="420" height="594" fill="url(#frontYellow)"/>
      <path d="M0 0 H420 V290 C330 280 300 215 210 205 C130 196 60 215 0 235 Z" fill="#6f6f6f"/>
      <path d="M0 0 H420 V262 C340 250 300 190 210 180 C130 172 60 190 0 212 Z" fill="url(#blackTop)"/>
      <path d="M0 212 C60 190 130 172 210 180 C300 190 340 250 420 262" fill="none" stroke="#2a2a2a" stroke-width="3"/>
      <path d="M0 540 L420 528 L420 572 L0 584 Z" fill="#0d0d0d"/>
    </svg>

    <p class="brand-name">Drum</p>
    <p class="tagline">customer insight</p>

    <h1 class="headline">
      <span class="small">Customer &amp;<br>Shopper Market</span>
      <span class="big">Research</span>
    </h1>

    <p class="web">www.drummr.com.au</p>
  </section>

</main>
</body>
</html>
```